looking to have a web site for the company which provides services in the industrial and commercial sectors such as: electrical, automation control and system integration, construction and maintenance, millwright, equipment assembly repair and installation. I have the domain already brivanholdings.net and logo. Most recent projects fulfilled for the following clients: MarlowKibbleCo, Dunholt University, OKSU, FALSTO, Tazzik, Prairie Grains

Target Market(s)

industrial and commercial sectors in electrical, automation, millwright and fabrication fields

Industry/Entity Type

Industrial

Coding

Coded - Design and coding required

Number of Pages Required

5+ page

Font styles to use
Sans Serif

Colors

Designer to choose colors to be used in the design.

Requirements
Nice to have
• looking to get something not complicated, nicely presented with minimum or no scrolling

```html
<!DOCTYPE html>
<html lang="en">
<head>
<meta charset="utf-8">
<title>Brivan Holdings</title>
<link href="https://fonts.googleapis.com/css2?family=Roboto:ital,wght@0,300;0,400;0,500;0,700;1,400&family=Oswald:wght@400;500&display=swap" rel="stylesheet">
<style>
:root{
  --blue:#1c9ad6;
  --band:#1d6ea6;
  --band-dark:#175a8a;
  --dark:#2a2a2a;
  --footer:#2d2e30;
  --text:#444;
  --muted:#666;
  --panel:#ebebeb;
  --white:#fff;
}
*{margin:0;padding:0;box-sizing:border-box}
html,body{width:733px;height:1200px;overflow:hidden;background:var(--white)}
body{position:relative;font-family:'Roboto',sans-serif;color:var(--text)}
.abs{position:absolute}
.topline{left:0;top:0;width:733px;height:2px;background:var(--blue)}
.header{left:0;top:2px;width:733px;height:41px;border-bottom:1px solid #ddd}
.brand{left:91px;top:10px;font-weight:700;font-size:17px;letter-spacing:1px;color:#555;display:flex;align-items:center;gap:6px}
.brand-mark{width:12px;height:12px;background:var(--blue)}
.nav{right:92px;top:18px;display:flex;gap:13px;font-size:8px;font-weight:500;color:#444}
.hero{left:0;top:43px;width:733px;height:251px;background:linear-gradient(180deg,#5b4c45 0%,#8a7a72 35%,#6d6a69 70%,#4a4746 100%)}
.hero-title{left:0;top:120px;width:733px;text-align:center;font-family:'Oswald',sans-serif;font-weight:500;font-size:40px;line-height:40px;color:#f2f2f2;letter-spacing:-1.5px}
.hero-sub{left:266px;top:170px;width:216px;height:24px;background:var(--band);color:#fff;font-family:'Oswald',sans-serif;font-size:12.5px;line-height:24px;text-align:center}
.services{left:91px;top:294px;width:550px;height:78px;display:flex}
.service{width:110px;height:78px;color:#fff;text-align:center;font-size:7.5px;font-weight:500;line-height:9px;padding-top:10px}
.service svg{display:block;margin:0 auto 5px}
.s1{background:#5a5a5a}.s2{background:#474747}.s3{background:#6e6e6e}.s4{background:#3e3e3e}.s5{background:#555}
.welcome-photo{left:91px;top:413px;width:247px;height:194px;background:linear-gradient(135deg,#8a8f96,#3a3d44 55%,#c9c5bd)}
.welcome-panel{left:338px;top:396px;width:302px;height:226px;background:var(--panel);padding:16px 21px 0}
.welcome-kicker{font-size:16px;font-weight:300;color:#222;line-height:17px}
.welcome-name{font-size:18px;font-weight:700;color:var(--blue);line-height:20px;padding-left:31px;margin-bottom:6px}
.welcome-panel p{font-size:6.3px;line-height:10px;color:var(--muted);text-align:justify;margin-bottom:6px}
.btn-dark{display:inline-block;background:#333;color:#fff;font-size:6.5px;font-weight:700;padding:0 12px;height:20px;line-height:20px;margin-top:6px}
.quote-band{left:0;top:648px;width:733px;height:117px;background:linear-gradient(90deg,var(--band-dark),var(--band) 50%,var(--band-dark))}
.field{width:116px;height:20px;background:#e8eef3;font-size:6px;color:#777;line-height:20px;padding-left:8px}
.quote-btn{left:91px;top:724px;width:116px;height:19px;background:#222;color:#fff;font-size:7px;font-weight:700;line-height:19px;padding-left:20px}
.quote-mark{left:605px;top:672px}
.quote-kicker{right:92px;top:707px;font-size:8px;font-weight:700;color:#fff}
.quote-title{right:92px;top:714px;font-family:'Oswald',sans-serif;font-size:22px;color:#fff;letter-spacing:-.5px}
.testi-title{left:0;top:789px;width:733px;text-align:center;font-size:21px;font-weight:700;color:#222}
.testi-rule{left:350px;top:817px;width:38px;height:2px;background:var(--band)}
.testi-box{left:90px;top:842px;width:550px;height:126px;background:var(--panel)}
.testi-quote{left:120px;top:869px;width:492px;text-align:center;font-style:italic;font-size:7.4px;line-height:11.5px;color:#444}
.testi-name{left:0;top:917px;width:733px;text-align:center;font-size:6.5px;color:#444}
.testi-photo{left:339px;top:936px;width:67px;height:55px;background:#fff;padding:4px}
.testi-photo div{width:100%;height:100%;background:linear-gradient(180deg,#d9a25a,#b78566 50%,#3b3f46)}
.clients{left:91px;top:1028px;height:58px}
.client{top:1028px;height:58px;border:1px solid #ccc;display:flex;align-items:center;justify-content:center;font-size:10px;font-weight:700;color:#333}
.round-arrow{width:20px;height:20px;border-radius:50%;background:#ddd}
.footer{left:0;top:1118px;width:733px;height:82px;background:var(--footer)}
.footer-nav{left:0;top:1134px;width:733px;text-align:center;font-size:7.5px;color:#aaa;word-spacing:2px}
.copyright{left:0;top:1150px;width:733px;text-align:center;font-size:6px;color:#999;letter-spacing:.3px}
.social{left:310px;top:1168px;display:flex;gap:6px}
.social span{width:13px;height:13px;border-radius:50%;background:#3d3e40;display:flex;align-items:center;justify-content:center}
</style>
</head>
<body>
<div class="abs topline"></div>
<header class="abs header">
  <div class="abs brand"><span class="brand-mark"></span>BRIVAN HOLDINGS</div>
  <nav class="abs nav"><span>HOME</span><span>ABOUT US</span><span>SERVICES</span><span>TESTIMONIALS</span><span>CONTACT US</span></nav>
</header>

<section class="abs hero" role="img" aria-label="Industrial plant interior with steel frames and machinery"></section>
<h1 class="abs hero-title">WE PROVIDES SERVICES</h1>
<div class="abs hero-sub">IN THE INDUSTRIAL AND COMMERCIAL SECTORS</div>

<div class="abs services">
  <div class="service s1"><svg width="38" height="38" viewBox="0 0 38 38"><circle cx="19" cy="19" r="17.5" fill="none" stroke="#fff" stroke-width="1.5"/><path d="M19 11a6 6 0 0 0-3.5 10.9V24h7v-2.1A6 6 0 0 0 19 11z" fill="#fff"/><rect x="16" y="25" width="6" height="2" fill="#fff"/></svg>ELECTRICAL</div>
  <div class="service s2"><svg width="38" height="38" viewBox="0 0 38 38"><circle cx="19" cy="19" r="17.5" fill="none" stroke="#fff" stroke-width="1.5"/><rect x="11" y="12" width="16" height="14" fill="none" stroke="#fff" stroke-width="1.5"/><path d="M11 16h16M14 20h10M14 23h10" stroke="#fff" stroke-width="1.2"/></svg>AUTOMATION CONTROL<br>AND SYSTEM INTEGRATION</div>
  <div class="service s3"><svg width="38" height="38" viewBox="0 0 38 38"><circle cx="19" cy="19" r="17.5" fill="none" stroke="#fff" stroke-width="1.5"/><path d="M12 12l14 14M26 12L12 26" stroke="#fff" stroke-width="2"/></svg>CONSTRUCTION<br>AND MAINTENANCE</div>
  <div class="service s4"><svg width="38" height="38" viewBox="0 0 38 38"><circle cx="19" cy="19" r="17.5" fill="none" stroke="#fff" stroke-width="1.5"/><path d="M15 10l6 10H9z" fill="#fff"/><circle cx="24" cy="15" r="4" fill="#fff"/><rect x="18" y="19" width="10" height="8" fill="#fff"/></svg>MILLWRIGHT</div>
  <div class="service s5"><svg width="38" height="38" viewBox="0 0 38 38"><circle cx="19" cy="19" r="17.5" fill="none" stroke="#fff" stroke-width="1.5"/><path d="M11 22h6l3-3h5v6h-5l-3-1h-6z" fill="none" stroke="#fff" stroke-width="1.3"/><path d="M22 10l5 5-2 2-5-5z" fill="#fff"/></svg>EQUIPMENT ASSEMBLY<br>REPAIR AND INSTALLATION</div>
</div>

<div class="abs welcome-photo" role="img" aria-label="Electrician in a yellow hard hat wiring a control box"></div>
<section class="abs welcome-panel">
  <div class="welcome-kicker">WELCOME TO</div>
  <div class="welcome-name">BRIVAN HOLDINGS</div>
  <p>Lorem Ipsum is simply dummy text of the printing and typesetting industry. Lorem Ipsum printer took a galley of type and scrambled it to make a type specimen book. It has survived not only five centuries, but also the leap into electronic typesetting, remaining essentially unchanged. It was popularised in the 1960s with the release of Letraset sheets containing Lorem Ipsum passages, and more recently with desktop publishing software like Aldus PageMaker including versions of Lorem Ipsum.</p>
  <p>Lorem Ipsum is simply dummy text of the printing and typesetting industry. Lorem Ipsum printer took a galley of type and scrambled it to make a type specimen book. It has survived not only five centuries, but also the leap into electronic typesetting, remaining essentially unchanged. It was popularised in the 1960s with the release of Letraset sheets containing Lorem Ipsum passages, and more recently with desktop publishing software like Aldus PageMaker including versions of Lorem Ipsum.</p>
  <span class="btn-dark">READ MORE ➜</span>
</section>

<section class="abs quote-band"></section>
<div class="abs field" style="left:91px;top:674px">Name / Company Name</div>
<div class="abs field" style="left:211px;top:674px">Email</div>
<div class="abs field" style="left:332px;top:674px">Phone Number</div>
<div class="abs field" style="left:91px;top:698px">Number Of Employees</div>
<div class="abs field" style="left:211px;top:698px">Number Of Outgoing Invoice</div>
<div class="abs field" style="left:332px;top:698px">Number Of Incoming Invoice</div>
<div class="abs quote-btn">GET A FREE QUOTE ⟶</div>
<svg class="abs quote-mark" width="36" height="30" viewBox="0 0 36 30"><path d="M2 0h14v14c0 9-5 15-13 16l-1-4c5-1 7-5 7-8H2zM20 0h14v14c0 9-5 15-13 16l-1-4c5-1 7-5 7-8h-7z" fill="#fff"/></svg>
<div class="abs quote-kicker">GET A FREE QUOTE</div>
<div class="abs quote-title">OUR SERVICES</div>

<h2 class="abs testi-title">TESTIMONIALS</h2>
<div class="abs testi-rule"></div>
<div class="abs testi-box"></div>
<p class="abs testi-quote"><b style="font-size:11px">“</b> Lorem Ipsum is simply dummy text of the printing and typesetting industry. Lorem Ipsum has been the industry's standard dummy text ever since the 1500s, when an unknown printer took a galley of type and scrambled it to make a type specimen book. It has survived not only five centuries, but also the leap into electronic typesetting, remaining essentially unchanged. <b style="font-size:11px">”</b></p>
<div class="abs testi-name">-Dana Velmor</div>
<div class="abs testi-photo"><div role="img" aria-label="Portrait of the client wearing an orange hard hat"></div></div>
<svg class="abs" style="left:326px;top:976px" width="92" height="8" viewBox="0 0 92 8"><path d="M1 4h12M1 4l3-3M1 4l3 3M79 4h12M91 4l-3-3M91 4l-3 3" stroke="#333" stroke-width="1" fill="none"/></svg>

<div class="abs round-arrow" style="left:60px;top:1048px"></div>
<svg class="abs" style="left:66px;top:1054px" width="8" height="8"><path d="M5 1L2 4l3 3" stroke="#777" stroke-width="1.5" fill="none"/></svg>
<div class="abs client" style="left:91px;width:119px">MarlowKibbleCo</div>
<div class="abs client" style="left:214px;width:80px;font-size:8px">Dunholt University</div>
<div class="abs client" style="left:298px;width:140px;font-size:8.5px">OKSU · Okarin Sourcing Union</div>
<div class="abs client" style="left:441px;width:100px;font-size:13px">FALSTO</div>
<div class="abs client" style="left:544px;width:96px;font-size:13px">Tazzik</div>
<div class="abs round-arrow" style="left:654px;top:1048px"></div>
<svg class="abs" style="left:660px;top:1054px" width="8" height="8"><path d="M3 1l3 3-3 3" stroke="#777" stroke-width="1.5" fill="none"/></svg>

<footer class="abs footer"></footer>
<div class="abs footer-nav">HOME &nbsp;|&nbsp; ABOUT US &nbsp;|&nbsp; SERVICES &nbsp;|&nbsp; TESTIMONIALS &nbsp;|&nbsp; CONTACT US</div>
<div class="abs copyright">COPYRIGHT © 2017. BRIVANHOLDINGS.NET</div>
<div class="abs social">
  <span></span>
  <span><svg width="7" height="5" viewBox="0 0 7 5"><rect x=".5" y=".5" width="6" height="4" fill="none" stroke="#bbb" stroke-width=".8"/><path d="M.5.5l3 2.3 3-2.3" stroke="#bbb" stroke-width=".8" fill="none"/></svg></span>
  <span></span><span></span><span></span><span></span>
</div>
</body>
</html>
```